Business Card Design

Company name is: Ridgeline Lifeguard Training, LLC. We teach CPR/AED, First Aid, Bloodborne Pathogens and other health and safety classes. Looking for an eye-catching, progressive, cutting edge design.

Industry/Entity Type

Health

Contact Information for Business Card

Tom Wexford (555.218.4073)
June Pellicott (555.862.1940)
email is info@ridgelinetraininghq.com
website is www.RidgelineTrainingHQ.com

```html
<!DOCTYPE html>
<html lang="en">
<head>
<meta charset="utf-8">
<title>Ridgeline Lifeguard Training – Business Card</title>
<link href="https://fonts.googleapis.com/css2?family=Arimo:wght@400&family=Carlito&family=Gelasio:wght@400&display=swap" rel="stylesheet">
<style>
  :root {
    --page: #e9e6e4;
    --card: #ffffff;
    --ink: #1b1b1b;
    --red: #e41f26;
    --orange: #ee6a1c;
    --aqua: #bfe6ea;
    --photo-a: #c9343a;
    --photo-b: #e8a14a;
    --photo-c: #8a4b8f;
  }
  html, body {
    margin: 0;
    width: 1200px;
    height: 800px;
    overflow: hidden;
    background: var(--page);
  }
  .card {
    position: absolute;
    left: 100px;
    top: 114px;
    width: 1000px;
    height: 572px;
    background: var(--card);
    overflow: hidden;
    box-shadow: 0 6px 24px rgba(0,0,0,.18);
  }
  .brand {
    position: absolute;
    left: 150px;
    top: 40px;
    width: 620px;
    text-align: center;
  }
  .brand-mark {
    display: block;
    width: 40px;
    height: 40px;
    margin: 0 auto 14px;
    border-radius: 50%;
    background: var(--red);
  }
  .brand-name {
    font-family: "Gelasio", serif;
    font-size: 40px;
    color: var(--ink);
    margin: 0;
    white-space: nowrap;
  }
  .brand-tagline {
    font-family: "Carlito", sans-serif;
    font-size: 17px;
    color: var(--red);
    margin: 6px 0 0;
    line-height: 1.2;
  }
  .contacts-band {
    position: absolute;
    left: 0;
    top: 250px;
    width: 710px;
    height: 130px;
    background: linear-gradient(90deg, var(--orange), var(--red) 70%);
    display: flex;
    align-items: center;
  }
  .person {
    flex: 1;
    padding-left: 40px;
    font-family: "Arimo", sans-serif;
    color: #fff;
  }
  .person + .person { border-left: 2px solid rgba(255,255,255,.8); }
  .person-name { font-size: 34px; margin: 0; }
  .person-phone { font-size: 27px; margin: 6px 0 0; }
  .web-band {
    position: absolute;
    left: 0;
    top: 380px;
    width: 710px;
    height: 192px;
    background: linear-gradient(90deg, #fff 0%, var(--aqua) 55%);
    font-family: "Arimo", sans-serif;
    font-size: 24px;
    color: var(--ink);
    padding: 28px 0 0 40px;
    box-sizing: border-box;
  }
  .web-band p { margin: 0 0 8px; }
  .training-photo {
    position: absolute;
    left: 710px;
    top: 210px;
    width: 290px;
    height: 362px;
    background: linear-gradient(160deg, var(--photo-c) 0%, var(--photo-a) 45%, var(--photo-b) 100%);
  }
</style>
</head>
<body>
  <main class="card">
    <header class="brand">
      <span class="brand-mark"></span>
      <h1 class="brand-name">Ridgeline Lifeguard Training, LLC</h1>
      <p class="brand-tagline">CPR/AED, First Aid, Bloodborne Pathogens<br>and other health and safety classes</p>
    </header>
    <section class="contacts-band">
      <div class="person">
        <p class="person-name">June Pellicott</p>
        <p class="person-phone">555.862.1940</p>
      </div>
      <div class="person">
        <p class="person-name">Tom Wexford</p>
        <p class="person-phone">555.218.4073</p>
      </div>
    </section>
    <section class="web-band">
      <p>Email : info@ridgelinetraininghq.com</p>
      <p>Web : www.RidgelineTrainingHQ.com</p>
    </section>
    <div class="training-photo" role="img" aria-label="Collage of CPR training: gloved hands practicing compressions and rescue breathing on manikins"></div>
  </main>
</body>
</html>
```